Website Required for Small Cyber Security Company

Require a website for Cyber Security company. I have logo which i will attach. Please use logo blue and white as a guide
Would ultimately like the site to have a technology theme with the following pages Landing page
Services
Contact
Careers

I can provide content for each of those pages in due course, until then happy for you to use dummy data to display purposes

Target Market(s)

Government

Industry/Entity Type

Cyber Security

Coding

Coded - Design and coding required

Number of Pages Required

4 page

Colors
0054AA
0677BA
7BADD7
CADEEF
E8F1F8

Requirements
Must have
• High quality finish and UX
Nice to have
• look and feel professional and not cheap

```html
<!DOCTYPE html>
<html lang="en">
<head>
<meta charset="utf-8">
<title>Harbor Ridge Consulting — Cyber Security</title>
<link rel="stylesheet" href="https://fonts.googleapis.com/css2?family=Source+Sans+3:wght@400;600;700&family=Barlow+Semi+Condensed:wght@500;600&display=swap">
<style>
:root{
  --navy:#0a1a3f;
  --navy-deep:#07132f;
  --blue:#0054aa;
  --blue-mid:#0677ba;
  --blue-bright:#1487c4;
  --sky:#7badd7;
  --ice:#cadeef;
  --white:#ffffff;
  --cyan:#5fd3f0;
  --footer:#1b1c21;
  --soc-dark:#111318;
}
*{margin:0;padding:0;box-sizing:border-box}
html,body{width:1200px;height:3512px;overflow:hidden}
body{font-family:"Source Sans 3",Arial,sans-serif;color:var(--white);background:var(--navy-deep);position:relative}
.abs{position:absolute}
section,header,footer{position:absolute;left:0;width:1200px;overflow:hidden}

/* header */
.site-header{top:0;height:120px;background:#182042;border-bottom:3px solid var(--blue-mid)}
.brand{left:172px;top:18px;display:flex;flex-direction:column;align-items:center;width:150px}
.brand-dot{width:48px;height:48px;border-radius:50%;border:4px solid var(--blue-mid)}
.brand-name{font-weight:600;font-size:19px;letter-spacing:.5px;margin-top:6px;color:var(--white)}
.brand-sub{font-size:10px;letter-spacing:3px;color:var(--white)}
.top-contact{top:22px;right:173px;display:flex;gap:18px;font-size:15px;align-items:center}
.top-contact span{display:flex;align-items:center;gap:10px}
.icon-box{width:26px;height:26px;border-radius:5px;background:var(--blue-mid);display:flex;align-items:center;justify-content:center}
.main-nav{top:74px;right:173px;display:flex;height:46px;font-size:18px}
.main-nav a{color:var(--white);text-decoration:none;padding:0 12px;line-height:42px}
.main-nav a.active{background:var(--blue-mid);border-radius:4px 4px 0 0;padding:0 14px}

/* hero */
.hero{top:120px;height:600px;background:radial-gradient(ellipse at 70% 40%,#153472 0%,#0b1d49 45%,#081638 100%)}
.hero h1{left:172px;top:100px;width:420px;font-size:49px;line-height:54px;font-weight:700}
.hero p{left:172px;top:283px;width:420px;font-size:15px;line-height:21px}
.btn{position:absolute;height:50px;display:flex;align-items:center;justify-content:center;font-weight:600;font-size:20px;border-radius:4px}
.btn-primary{left:172px;top:356px;width:135px;background:var(--blue-mid)}
.btn-outline{left:323px;top:356px;width:134px;border:2px solid var(--white)}
.hero-art{left:652px;top:105px;width:450px;height:427px;border-radius:30px;background:radial-gradient(circle at 45% 45%,#3aa0ff 0%,#1a62d6 40%,#13286a 75%,rgba(10,26,63,0) 100%)}

/* solutions */
.solutions{top:720px;height:576px;background:radial-gradient(ellipse at 50% 50%,#0b4aa0 0%,#0a3277 55%,#0a2458 100%)}
.section-title{width:1200px;left:0;text-align:center;font-weight:600;font-size:38px}
.solutions .section-title{top:62px}
.card{top:152px;width:272px;height:342px;border:2px solid var(--blue-bright);border-radius:10px;overflow:hidden;background:var(--navy)}
.card .card-top{height:138px;background:var(--blue-mid);border-radius:0 0 50% 50%/0 0 14px 14px;display:flex;align-items:center;justify-content:center}
.card-art{width:84px;height:84px;border-radius:18px;background:radial-gradient(circle,#6fc2ff 0%,#2a7de0 60%,rgba(0,0,0,0) 100%)}
.card h3{font-family:"Barlow Semi Condensed",Arial,sans-serif;font-weight:600;font-size:26px;text-align:center;margin-top:24px}
.card p{font-size:15px;line-height:21px;text-align:center;padding:0 18px;margin-top:6px}
.card .read{display:block;margin:18px auto 0;width:106px;height:38px;border:2px solid var(--white);border-radius:5px;font-weight:600;font-size:16px;line-height:34px;text-align:center;background:var(--blue-mid)}
.card.alt{background:var(--blue-mid)}
.card.alt .card-top{background:var(--navy)}
.card.alt .read{background:var(--navy)}

/* soc */
.soc{top:1296px;height:580px;background:linear-gradient(100deg,#0d0f14 0%,#1c1d22 45%,#2d2722 100%)}
.soc-art{left:48px;top:68px;width:410px;height:430px;border-radius:48% 48% 45% 45%;background:radial-gradient(circle at 55% 45%,#8fe4ff 0%,#1a8fd0 35%,#0d3a66 70%,rgba(13,15,20,0) 100%)}
.soc h2{left:514px;top:98px;font-size:41px;line-height:46px;font-weight:600}
.soc p{left:514px;top:207px;width:513px;font-size:15px;line-height:21px;text-align:justify}
.feature-list{left:514px;top:338px;width:513px;display:grid;grid-template-columns:232px 232px;row-gap:15px;list-style:none;font-size:15px}
.feature-list li{display:flex;align-items:center;gap:11px}

/* perfect solution */
.protection{top:1876px;height:709px;background:radial-gradient(ellipse at 50% 55%,#123b85 0%,#0c2a62 55%,#0b2250 100%)}
.protection .section-title{top:58px}
.protection .lead{left:340px;width:520px;top:114px;text-align:center;font-size:15px;line-height:21px}
.hub-ring{left:434px;top:232px;width:332px;height:332px;border-radius:50%;border:3px solid var(--white)}
.hub-name{left:480px;top:380px;width:240px;text-align:center;font-weight:600;font-size:26px;color:var(--sky);letter-spacing:1px}
.node{width:60px;height:60px;border-radius:50%;background:var(--ice);border:3px solid var(--white);display:flex;align-items:center;justify-content:center}
.node-label h4{font-family:"Barlow Semi Condensed",Arial,sans-serif;font-weight:500;font-size:22px}
.node-label p{font-size:15px;margin-top:2px}
.right{text-align:right}

/* testimonials */
.testimonials{top:2585px;height:505px;background:radial-gradient(ellipse at 30% 30%,#1b3466 0%,#132650 60%,#0f1f44 100%)}
.testimonials h2{left:172px;top:92px;font-size:38px;font-weight:600}
.quote{left:172px;top:160px;width:478px;font-size:20px;line-height:36px;text-align:justify}
.author{left:172px;top:284px;font-size:20px}
.dots{left:172px;top:347px;display:flex;gap:8px}
.dots i{width:14px;height:14px;border-radius:50%;background:#9aa7c0}
.dots i:first-child{background:var(--white)}
.portrait{left:674px;top:102px;width:300px;height:300px;border-radius:50%;border:4px solid var(--blue-bright);background:radial-gradient(circle at 50% 40%,#eef1f4 0%,#d9dde2 55%,#7a3a3a 100%)}

/* footer */
.site-footer{top:3090px;height:422px;background:var(--footer)}
.footer-brand{left:177px;top:66px;width:332px;display:flex;flex-direction:column;align-items:center}
.footer-brand .brand-dot{width:120px;height:120px;border-width:8px}
.footer-brand .brand-name{font-size:44px;margin-top:12px;letter-spacing:1px}
.footer-brand .brand-sub{font-size:18px;letter-spacing:6px;color:var(--sky)}
.footer-col h5{font-size:22px;font-weight:600}
.quick-links{left:604px;top:80px}
.quick-links ul{list-style:none;margin-top:16px}
.quick-links li{font-size:15px;line-height:29.5px}
.touch{left:806px;top:80px}
.touch .row{display:flex;gap:12px;font-size:15px;line-height:20px;margin-top:18px;align-items:flex-start}
.touch .row:first-of-type{margin-top:22px}
.footer-rule{left:172px;top:350px;width:855px;height:1px;background:#8a8f99}
.copyright{left:0;width:1200px;top:374px;text-align:center;font-size:14px}
</style>
</head>
<body>

<header class="site-header">
  <div class="abs brand"><div class="brand-dot"></div><div class="brand-name">HARBOR RIDGE</div><div class="brand-sub">CONSULTING</div></div>
  <div class="abs top-contact">
    <span><i class="icon-box"><svg width="16" height="12" viewBox="0 0 16 12"><rect x="1" y="1" width="14" height="10" fill="none" stroke="#fff" stroke-width="1.5"/><path d="M1 1l7 6 7-6" fill="none" stroke="#fff" stroke-width="1.5"/></svg></i>info@harborridge.example</span>
    <span><i class="icon-box"><svg width="14" height="14" viewBox="0 0 24 24"><path d="M6.6 10.8a15 15 0 006.6 6.6l2.2-2.2c.3-.3.7-.4 1-.2 1.1.4 2.3.6 3.6.6.6 0 1 .4 1 1V20c0 .6-.4 1-1 1A17 17 0 013 4c0-.6.4-1 1-1h3.5c.6 0 1 .4 1 1 0 1.3.2 2.5.6 3.6.1.3 0 .7-.2 1z" fill="#fff"/></svg></i>+ 123 555 0199</span>
  </div>
  <nav class="abs main-nav">
    <a class="active">Home</a><a>About Us</a><a>Services</a><a>Pricing</a><a>Blog</a><a>Contact Us</a>
  </nav>
</header>

<section class="hero">
  <h1 class="abs">We Provide Cyber Solutions For Your Security.</h1>
  <p class="abs">Quis autem vel eum iure reprehenderit qui in ea voluptate velit esse ruam nihil molestiae.</p>
  <a class="btn btn-primary">Get Started</a>
  <a class="btn btn-outline">Contact Us</a>
  <div class="abs hero-art" role="img" aria-label="3D illustration of a browser window with a blue security shield and check mark"></div>
</section>

<section class="solutions">
  <h2 class="section-title abs">Cyber Security Solutions</h2>
  <article class="abs card" style="left:172px">
    <div class="card-top"><div class="card-art" role="img" aria-label="Fingerprint scanner illustration"></div></div>
    <h3>Finger Print Security</h3>
    <p>Quis autem vel eum iure reprehenderit qui in ea voluptate velit esse ruam nihil molestiae.</p>
    <a class="read">Read More</a>
  </article>
  <article class="abs card alt" style="left:465px">
    <div class="card-top"><div class="card-art" role="img" aria-label="Server rack illustration"></div></div>
    <h3>Server Security</h3>
    <p>Quis autem vel eum iure reprehenderit qui in ea voluptate velit esse ruam nihil molestiae.</p>
    <a class="read">Read More</a>
  </article>
  <article class="abs card" style="left:756px">
    <div class="card-top"><div class="card-art" role="img" aria-label="Laptop with padlock and chains illustration"></div></div>
    <h3>Computer Security</h3>
    <p>Quis autem vel eum iure reprehenderit qui in ea voluptate velit esse ruam nihil molestiae.</p>
    <a class="read">Read More</a>
  </article>
</section>

<section class="soc">
  <div class="abs soc-art" role="img" aria-label="Glowing digital shield with a keyhole lock"></div>
  <h2 class="abs">24/7 Cyber Security<br>Operation Center</h2>
  <p class="abs">Duis aute irure dolor in reprehenderit in voluptate esse cillu dolore eu fugiat nulla pariatur excepteur sint occaecat cupia at non proident, sunt in culpa rui officia deserunt mollit ani mid est laborum incidunt aut labore magnam. Occaecat cupia at non proident, sunt in culpa rui officia deserunt mollit ani mid est laborum incidunt aut labore magnam.</p>
  <ul class="abs feature-list">
    <li><svg width="14" height="14" viewBox="0 0 24 24"><path d="M12 2l3 7h7l-5.5 4.5 2 7.5L12 16.5 5.5 21l2-7.5L2 9h7z" fill="#5fd3f0"/></svg>Malware Detection Removal</li>
    <li><svg width="14" height="14" viewBox="0 0 24 24"><path d="M12 2l3 7h7l-5.5 4.5 2 7.5L12 16.5 5.5 21l2-7.5L2 9h7z" fill="#5fd3f0"/></svg>Cloud Security</li>
    <li><svg width="14" height="14" viewBox="0 0 24 24"><path d="M12 2l3 7h7l-5.5 4.5 2 7.5L12 16.5 5.5 21l2-7.5L2 9h7z" fill="#5fd3f0"/></svg>Content Delivery Network</li>
    <li><svg width="14" height="14" viewBox="0 0 24 24"><path d="M12 2l3 7h7l-5.5 4.5 2 7.5L12 16.5 5.5 21l2-7.5L2 9h7z" fill="#5fd3f0"/></svg>Cyber Security</li>
    <li><svg width="14" height="14" viewBox="0 0 24 24"><path d="M12 2l3 7h7l-5.5 4.5 2 7.5L12 16.5 5.5 21l2-7.5L2 9h7z" fill="#5fd3f0"/></svg>Security Management</li>
    <li><svg width="14" height="14" viewBox="0 0 24 24"><path d="M12 2l3 7h7l-5.5 4.5 2 7.5L12 16.5 5.5 21l2-7.5L2 9h7z" fill="#5fd3f0"/></svg>Identifying Threats</li>
    <li><svg width="14" height="14" viewBox="0 0 24 24"><path d="M12 2l3 7h7l-5.5 4.5 2 7.5L12 16.5 5.5 21l2-7.5L2 9h7z" fill="#5fd3f0"/></svg>SIEM Threat Detection</li>
    <li><svg width="14" height="14" viewBox="0 0 24 24"><path d="M12 2l3 7h7l-5.5 4.5 2 7.5L12 16.5 5.5 21l2-7.5L2 9h7z" fill="#5fd3f0"/></svg>Server Security</li>
  </ul>
</section>

<section class="protection">
  <h2 class="section-title abs">The Perfect Solution For all Protection</h2>
  <p class="abs lead">Qugiat nulla pariatur excepteur sint occaecat cupidatat no proident, sunt in culpa rui officia deserunt.</p>
  <div class="abs hub-ring"></div>
  <div class="abs hub-name">HARBOR RIDGE</div>

  <div class="abs node" style="left:428px;top:242px"><svg width="28" height="28" viewBox="0 0 24 24" fill="none" stroke="#1b2c55" stroke-width="1.8"><ellipse cx="12" cy="5" rx="7" ry="2.5"/><path d="M5 5v12c0 1.4 3 2.5 7 2.5M19 5v7M5 11c0 1.4 3 2.5 7 2.5s7-1.1 7-2.5"/></svg></div>
  <div class="abs node" style="left:712px;top:242px"><svg width="28" height="28" viewBox="0 0 24 24" fill="none" stroke="#1b2c55" stroke-width="1.8"><circle cx="12" cy="7" r="4"/><path d="M4 21c0-4 3.6-7 8-7s8 3 8 7z"/></svg></div>
  <div class="abs node" style="left:411px;top:372px"><svg width="28" height="28" viewBox="0 0 24 24" fill="none" stroke="#1b2c55" stroke-width="1.8"><rect x="6" y="10" width="12" height="10" rx="1"/><path d="M8.5 10V7a3.5 3.5 0 017 0v3"/></svg></div>
  <div class="abs node" style="left:728px;top:372px"><svg width="30" height="28" viewBox="0 0 24 24" fill="none" stroke="#1b2c55" stroke-width="1.8"><circle cx="12" cy="12" r="1.6" fill="#1b2c55"/><path d="M8.5 8.5a5 5 0 000 7M15.5 8.5a5 5 0 010 7M5.5 5.5a9 9 0 000 13M18.5 5.5a9 9 0 010 13"/></svg></div>
  <div class="abs node" style="left:570px;top:495px"><svg width="28" height="28" viewBox="0 0 24 24" fill="none" stroke="#1b2c55" stroke-width="1.8"><circle cx="12" cy="12" r="9"/><path d="M3 12h18M12 3c3 3 3 15 0 18M12 3c-3 3-3 15 0 18"/></svg></div>

  <div class="abs node-label right" style="right:784px;top:236px"><h4>Cloud Solutions</h4><p>Ruis autem vel eum rui inea elit niau</p></div>
  <div class="abs node-label" style="left:784px;top:236px"><h4>Cyber Solutions</h4><p>Ruis autem vel eum rui inea elit niau.</p></div>
  <div class="abs node-label right" style="right:806px;top:372px"><h4>Locker Security</h4><p>Ruis autem vel eum rui inea elit niau</p></div>
  <div class="abs node-label" style="left:806px;top:372px"><h4>Network Security</h4><p>Ruis autem vel eum rui inea elit niau.</p></div>
  <div class="abs node-label" style="left:400px;width:400px;text-align:center;top:570px"><h4>Web Security</h4><p>Ruis autem vel eum rui inea elit niau</p></div>
</section>

<section class="testimonials">
  <h2 class="abs">Client Testimonials</h2>
  <p class="abs quote">“Quis autem vel eum iure reprehenderit aui in ea voluptate velit esse quam nihil molestiae consequatur, vel illum qui dolorem eum fugiat voluptas pariatur.”</p>
  <p class="abs author">- Daniel Moreau</p>
  <div class="abs dots"><i></i><i></i><i></i></div>
  <div class="abs portrait" role="img" aria-label="Portrait photo of the client"></div>
</section>

<footer class="site-footer">
  <div class="abs footer-brand"><div class="brand-dot"></div><div class="brand-name">HARBOR RIDGE</div><div class="brand-sub">CONSULTING</div></div>
  <div class="abs footer-col quick-links">
    <h5>Quick Links</h5>
    <ul><li>Home</li><li>About Us</li><li>Services</li><li>Pricing</li><li>Blog</li><li>Contact Us</li></ul>
  </div>
  <div class="abs footer-col touch">
    <h5>Get In Touch</h5>
    <div class="row"><i class="icon-box"><svg width="14" height="14" viewBox="0 0 24 24"><path d="M6.6 10.8a15 15 0 006.6 6.6l2.2-2.2c.3-.3.7-.4 1-.2 1.1.4 2.3.6 3.6.6.6 0 1 .4 1 1V20c0 .6-.4 1-1 1A17 17 0 013 4c0-.6.4-1 1-1h3.5c.6 0 1 .4 1 1 0 1.3.2 2.5.6 3.6.1.3 0 .7-.2 1z" fill="#fff"/></svg></i><span style="padding-top:3px">+ 123 555 0199</span></div>
    <div class="row"><i class="icon-box"><svg width="16" height="12" viewBox="0 0 16 12"><rect x="1" y="1" width="14" height="10" fill="none" stroke="#fff" stroke-width="1.5"/><path d="M1 1l7 6 7-6" fill="none" stroke="#fff" stroke-width="1.5"/></svg></i><span style="padding-top:3px">info@harborridge.example</span></div>
    <div class="row"><i class="icon-box"><svg width="14" height="16" viewBox="0 0 24 24"><path d="M12 2a7 7 0 00-7 7c0 5 7 13 7 13s7-8 7-13a7 7 0 00-7-7z" fill="none" stroke="#fff" stroke-width="2"/><circle cx="12" cy="9" r="2.5" fill="#fff"/></svg></i><span style="padding-top:3px">48 Elm Row Seaford,<br>4100, Australia</span></div>
  </div>
  <div class="abs footer-rule"></div>
  <p class="abs copyright">Copyrights @ 2023 Harbor Ridge All Rights Reserved</p>
</footer>

</body>
</html>
```